Gilded Canopy Decor Rentals Spain

Why not add the WOW factor to your special occassion by bringing it to life with our beautiful selection of magnificent Blosom Tree´s.
Handmade with Silk Flowers these Tree´s look real to life adding the perfect decoration to your event or breathtaking feature for your Wedding Day.
Our Tree´s suit any theme whether its Rustic, Elegant, Fairy Tale or Enhanted.
With a versitle selection we offerf floor to ceiling and table centre pieces which can be used both inside or outdoor.
If you are looking for your Fiary Tale look no further.
Target Market(s)
Franchise , weddings and Events
Font styles to use
Requirements
Must have
- Crisp Lettering and attractive Presintation
Nice to have
- Elegant fonts and different from the rest
I am looking for a overall branding design ,including letter heads Buisness cards email signuture a4 template design ,invoising design ,Presentation folder design to hold A4 papers and usb stick ,envolope design ,flyier design ,three font designs sticker design, New logo design 3 concepts

```html
<!DOCTYPE html>
<html lang="en">
<head>
<meta charset="utf-8">
<title>Gilded Canopy Decor Rentals Spain — Stationery Set</title>
<link rel="stylesheet" href="https://fonts.googleapis.com/css2?family=Patrick+Hand&family=Open+Sans:wght@400&display=swap">
<style>
  :root{
    --canvas:#adacb1;
    --ink:#1e1e1f;
    --ink-deep:#0b0b0b;
    --ink-soft:#2d2d30;
    --paper:#ffffff;
    --paper-grey:#dcdcdc;
    --brand-red:#b5060f;
    --text-grey:#555558;
    --ring-grey:#c9c9cc;
  }
  html,body{margin:0;padding:0;width:1200px;height:800px;overflow:hidden;background:var(--canvas);}
  .stationery-set{display:block;width:1200px;height:800px;}
  .brand-name{font-family:"Patrick Hand",cursive;letter-spacing:.5px;}
  .headline{font-family:"Patrick Hand",cursive;font-size:26px;fill:var(--text-grey);letter-spacing:1px;}
  .body-copy{font-family:"Open Sans",sans-serif;font-size:8px;fill:var(--text-grey);}
  .contact{font-family:"Open Sans",sans-serif;font-size:4.2px;fill:var(--text-grey);}
</style>
</head>
<body>
<svg class="stationery-set" viewBox="0 0 1500 1000" xmlns="http://www.w3.org/2000/svg" role="img" aria-label="Gilded Canopy Decor Rentals Spain stationery set">
  <defs>
    <linearGradient id="sheen" x1="0" y1="0" x2="1" y2="0">
      <stop offset="0" stop-color="#ffffff"/>
      <stop offset="1" stop-color="#a9a9ab"/>
    </linearGradient>
    <filter id="lift" x="-5%" y="-5%" width="115%" height="115%">
      <feDropShadow dx="3" dy="4" stdDeviation="3" flood-color="#000" flood-opacity=".25"/>
    </filter>
  </defs>

  <!-- Letterhead -->
  <g class="letterhead" transform="translate(89 82)" filter="url(#lift)">
    <rect width="302" height="426" fill="var(--paper)"/>
    <path d="M0 0H190L110 80Q95 95 75 95H0Z" fill="url(#sheen)"/>
    <path d="M0 95H75Q95 95 110 80L190 0" fill="none" stroke="var(--brand-red)" stroke-width="3"/>
    <path d="M0 98H78Q98 98 113 83L196 0H253L128 125Q112 138 90 138H0Z" fill="var(--ink)"/>
    <path d="M302 240L205 337Q192 350 192 365V426H302Z" fill="var(--paper-grey)"/>
    <circle cx="242" cy="80" r="20" fill="var(--ring-grey)"/>
    <text class="brand-name" x="242" y="114" font-size="5" text-anchor="middle" fill="var(--text-grey)">GILDED CANOPY DECOR RENTALS SPAIN</text>
    <text class="headline" x="45" y="180">HEADLINE</text>
    <text class="body-copy" x="45" y="218">Lorem ipsum dolor sit amet, consectetur adipiscing elit.</text>
    <text class="body-copy" x="45" y="228">Etiam iaculis commodo.</text>
    <text class="body-copy" x="45" y="277">Lorem ipsum dolor sit amet, consectetur adipiscing elit.</text>
    <text class="body-copy" x="45" y="287">Etiam iaculis commod.</text>
    <line x1="45" y1="364" x2="118" y2="364" stroke="var(--text-grey)" stroke-width="1"/>
    <line x1="172" y1="364" x2="246" y2="364" stroke="var(--text-grey)" stroke-width="1"/>
  </g>

  <!-- Presentation folder -->
  <g class="folder" transform="translate(421 82)" filter="url(#lift)">
    <rect width="302" height="426" fill="var(--ink)"/>
    <path d="M0 133H115Q135 133 150 118L270 0H302V22L178 160Q160 180 138 180H0Z" fill="var(--ink-soft)"/>
    <path d="M0 0H265L130 120Q115 133 100 133H0Z" fill="url(#sheen)"/>
    <path d="M0 133H115Q133 133 148 118L265 0" fill="none" stroke="var(--brand-red)" stroke-width="3"/>
    <circle cx="152" cy="251" r="15" fill="var(--brand-red)"/>
    <text class="brand-name" x="152" y="286" font-size="12" text-anchor="middle" fill="var(--paper)">GILDED CANOPY DECOR RENTALS SPAIN</text>
    <circle cx="131" cy="399" r="7" fill="var(--paper)"/>
    <circle cx="151" cy="399" r="7" fill="var(--paper)"/>
    <circle cx="171" cy="399" r="7" fill="var(--paper)"/>
  </g>

  <!-- USB drive with cable -->
  <g class="usb-drive">
    <path d="M867 215V125Q867 97 900 97Q935 97 935 125V200Q935 236 970 236H990Q1020 236 1020 266V470" fill="none" stroke="var(--ink-deep)" stroke-width="3"/>
    <rect x="850" y="212" width="35" height="50" rx="4" fill="var(--ink-deep)"/>
    <rect x="1003" y="462" width="37" height="58" rx="6" fill="var(--ink-deep)"/>
    <rect x="1006" y="518" width="28" height="17" fill="#6b6b6e"/>
    <rect x="770" y="260" width="193" height="264" rx="14" fill="var(--ink)" filter="url(#lift)"/>
    <rect x="784" y="272" width="165" height="237" rx="10" fill="#262628"/>
    <circle cx="799" cy="282" r="3" fill="var(--brand-red)"/>
  </g>

  <!-- Business card, front -->
  <g class="business-card-front" filter="url(#lift)">
    <rect x="1011" y="105" width="181" height="106" fill="var(--ink)"/>
    <circle cx="1104" cy="151" r="10" fill="var(--brand-red)"/>
    <text class="brand-name" x="1104" y="174" font-size="4.5" text-anchor="middle" fill="var(--paper)">GILDED CANOPY DECOR RENTALS SPAIN</text>
  </g>

  <!-- Business card, back -->
  <g class="business-card-back" filter="url(#lift)">
    <rect x="1238" y="105" width="182" height="106" fill="var(--paper)"/>
    <text class="contact" x="1390" y="124" text-anchor="end" fill="var(--brand-red)" style="fill:var(--brand-red)">INFO@GILDEDCANOPY.ES</text>
    <text class="contact" x="1410" y="132" text-anchor="end">WWW.GILDEDCANOPY.ES</text>
    <text class="contact" x="1403" y="142" text-anchor="end">+34 960 123 456</text>
    <text class="contact" x="1403" y="147" text-anchor="end">CALLE MAYOR 12</text>
    <text class="contact" x="1403" y="152" text-anchor="end">46001 VALENCIA</text>
    <text class="contact" x="1403" y="157" text-anchor="end">SPAIN</text>
    <circle cx="1256" cy="195" r="5" fill="var(--ink)"/>
    <circle cx="1270" cy="195" r="5" fill="var(--ink)"/>
    <circle cx="1285" cy="195" r="5" fill="var(--ink)"/>
  </g>

  <!-- Envelope -->
  <g class="envelope" filter="url(#lift)">
    <path d="M89 716L265 595Q280 580 297 595L463 716Z" fill="#1d1d1d"/>
    <rect x="89" y="716" width="374" height="179" fill="#121212"/>
    <path d="M89 716H463L360 800H195Z" fill="#030303"/>
    <path d="M89 895V720L235 790Q250 778 276 778Q302 778 317 790L463 720V895Z" fill="#1a1a1a"/>
    <circle cx="276" cy="802" r="15" fill="var(--brand-red)"/>
  </g>

  <!-- Pencils -->
  <g class="pencils">
    <polygon points="538,598 555,598 555,873 538,873" fill="var(--ink)"/>
    <rect x="538" y="590" width="17" height="10" fill="#e98b8b"/>
    <polygon points="538,873 555,873 546,893" fill="#f0b27a"/>
    <rect x="543" y="705" width="5" height="36" fill="var(--paper)"/>
    <polygon points="587,610 604,610 604,873 587,873" fill="var(--brand-red)"/>
    <polygon points="587,610 604,610 595,590" fill="#f0b27a"/>
    <rect x="587" y="873" width="17" height="18" fill="#f2f2f2"/>
    <text class="brand-name" transform="translate(594 690) rotate(90)" font-size="4" fill="var(--paper)">GILDED CANOPY DECOR</text>
  </g>

  <!-- Spiral notebook -->
  <g class="notebook">
    <rect x="692" y="583" width="239" height="350" fill="var(--ink)" filter="url(#lift)"/>
    <g class="spiral" fill="#d9d9db">
      <circle cx="704" cy="600" r="5"/><circle cx="704" cy="621" r="5"/><circle cx="704" cy="642" r="5"/><circle cx="704" cy="663" r="5"/>
      <circle cx="704" cy="684" r="5"/><circle cx="704" cy="704" r="5"/><circle cx="704" cy="725" r="5"/><circle cx="704" cy="746" r="5"/>
      <circle cx="704" cy="767" r="5"/><circle cx="704" cy="788" r="5"/><circle cx="704" cy="809" r="5"/><circle cx="704" cy="830" r="5"/>
      <circle cx="704" cy="850" r="5"/><circle cx="704" cy="871" r="5"/><circle cx="704" cy="892" r="5"/><circle cx="704" cy="913" r="5"/>
    </g>
    <g stroke="#d9d9db" stroke-width="2">
      <path d="M676 600H704M676 621H704M676 642H704M676 663H704M676 684H704M676 704H704M676 725H704M676 746H704M676 767H704M676 788H704M676 809H704M676 830H704M676 850H704M676 871H704M676 892H704M676 913H704"/>
    </g>
    <circle cx="817" cy="659" r="15" fill="var(--brand-red)"/>
    <text class="brand-name" x="827" y="696" font-size="9" text-anchor="middle" fill="var(--paper)">GILDED CANOPY DECOR RENTALS SPAIN</text>
  </g>

  <!-- Tote bag -->
  <g class="tote-bag" filter="url(#lift)">
    <path d="M1160 325L1200 282H1293L1333 325V480Q1333 495 1310 495Q1287 495 1287 480V325H1208V480Q1208 495 1185 495Q1160 495 1160 480Z" fill="var(--ink-deep)"/>
    <rect x="1071" y="446" width="348" height="478" fill="var(--ink)"/>
    <path d="M1160 446V480Q1160 495 1185 495Q1208 495 1208 480V446ZM1287 446V480Q1287 495 1310 495Q1333 495 1333 480V446Z" fill="var(--ink-deep)"/>
    <line x1="1071" y1="467" x2="1419" y2="467" stroke="#111" stroke-width="2"/>
    <line x1="1071" y1="898" x2="1419" y2="898" stroke="#111" stroke-width="2"/>
    <circle cx="1247" cy="534" r="18" fill="var(--brand-red)"/>
    <text class="brand-name" x="1257" y="570" font-size="10" text-anchor="middle" fill="var(--paper)">GILDED CANOPY DECOR RENTALS SPAIN</text>
  </g>
</svg>
</body>
</html>
```